Web page for Gareth Pemblewick Chartered Tax Adviser

I need to take the basic web page that I have created and "Brand it" to be compatible with the corporate logo and stationery created for me by other Studio Flock designers.
I will need a watermark as well as a distinctive home page and then a branded general page for content including a series of Blogs.

Target Market(s)

My practice deals with expatriates including those looking to invest in Australia.

Industry/Entity Type

Crowd

Font styles to use
Other font styles liked:
• Per logo

Requirements
Must have
• Besides the homepage I will need a general page for content, branded in the same style as the letterheads.
Nice to have
• A watermark to go with the blogs and news content.

```html
<!DOCTYPE html>
<html lang="en">
<head>
<meta charset="utf-8">
<title>Gareth Pemblewick — Chartered Tax Adviser</title>
<link rel="stylesheet" href="https://fonts.googleapis.com/css2?family=Josefin+Slab:wght@300;400;600;700&family=Open+Sans:wght@400;600&display=swap">
<style>
:root{
  --navy:#1c2f56;
  --navy-deep:#16264a;
  --steel:#24466b;
  --ink:#3a3a3a;
  --grey-band:#d6d6d6;
  --grey-review:#cdcdcd;
  --grey-soft:#c9c9c9;
  --white:#ffffff;
  --link:#3d8fd6;
}
*{margin:0;padding:0;box-sizing:border-box}
html,body{width:1200px;height:2412px;overflow:hidden}
body{position:relative;background:var(--white);font-family:"Open Sans",Arial,sans-serif;color:var(--ink)}
.abs{position:absolute}
.slab{font-family:"Josefin Slab",Georgia,serif}

/* hero */
.hero-photo{left:0;top:60px;width:1200px;height:600px;
  background:linear-gradient(90deg,#ffffff 0%,#eef2f4 30%,#d7e2e4 55%,#c9d6da 75%,#bfcdd2 100%)}
.hero-curves{left:0;top:0;width:1200px;height:700px}

.brand{left:168px;top:22px;display:flex;align-items:center;gap:10px;color:var(--navy)}
.brand-dot{width:44px;height:44px;border-radius:50%;background:var(--navy)}
.brand-name{font-family:"Josefin Slab",Georgia,serif;font-weight:600;font-size:21px;line-height:1.05;letter-spacing:.5px}
.brand-name small{display:block;font-size:11px;letter-spacing:2.5px}

.nav{left:588px;top:38px;display:flex;gap:34px;font-family:"Josefin Slab",Georgia,serif;font-size:13px;font-weight:600;color:var(--navy);letter-spacing:.5px}
.nav a{color:inherit;text-decoration:none;padding-bottom:8px}
.nav a.active{border-bottom:2px solid var(--navy)}

.social{display:flex;gap:10px}
.social span{width:36px;height:40px;background:#e3e3e3;clip-path:polygon(50% 0,100% 25%,100% 75%,50% 100%,0 75%,0 25%)}
.social-top{left:244px;top:96px}

.hero-lead{left:176px;top:298px;font-size:25px;font-weight:700;color:var(--navy);letter-spacing:.5px}
.hero-title{left:172px;top:320px;font-size:76px;font-weight:700;color:var(--navy-deep);letter-spacing:1px}
.btn{display:flex;align-items:center;justify-content:center;background:var(--navy);color:var(--white);font-family:"Josefin Slab",Georgia,serif;font-weight:600;font-size:12px;letter-spacing:.5px;text-decoration:none}
.hero-btn{left:276px;top:418px;width:196px;height:60px;font-size:14px}
.dots{display:flex;gap:6px}
.dots i{width:14px;height:16px;background:#9a9a9a;clip-path:polygon(50% 0,100% 25%,100% 75%,50% 100%,0 75%,0 25%)}
.dots i.on{background:var(--navy)}
.hero-dots{left:346px;top:508px}

.hero-contact{left:842px;top:580px;display:flex;flex-direction:column;gap:12px;font-size:11px;color:#777}
.hero-contact div{display:flex;align-items:center;gap:12px}
.hex-ico{width:22px;height:24px;background:var(--navy);clip-path:polygon(50% 0,100% 25%,100% 75%,50% 100%,0 75%,0 25%);display:flex;align-items:center;justify-content:center}

/* statement */
.statement{left:0;top:718px;width:1200px;text-align:center;font-family:"Josefin Slab",Georgia,serif;font-weight:300;font-size:86px;line-height:86px;color:var(--steel);letter-spacing:2px}
.statement b{font-weight:700}

/* welcome */
.welcome{left:0;top:1060px;width:1200px;height:132px;background:var(--grey-band)}
.welcome-title{left:172px;top:1090px;color:var(--navy)}
.welcome-title h2{font-family:"Josefin Slab",Georgia,serif;font-size:36px;font-weight:700;letter-spacing:1px}
.welcome-title p{font-family:"Josefin Slab",Georgia,serif;font-size:21px;letter-spacing:1px;margin-top:-4px}
.welcome-text{left:420px;top:1097px;width:400px;font-size:10.5px;line-height:13px;color:#555}
.welcome-btn{left:842px;top:1098px;width:185px;height:56px}

/* services */
.section-title{left:0;width:1200px;text-align:center;font-family:"Josefin Slab",Georgia,serif;font-size:42px;font-weight:600;color:var(--steel);letter-spacing:1px}
.section-sub{left:0;width:1200px;text-align:center;font-family:"Josefin Slab",Georgia,serif;font-size:13px;font-weight:600;color:#666;letter-spacing:.5px}
.service{width:240px;text-align:center}
.service svg{display:block;margin:0 auto}
.service h3{font-family:"Josefin Slab",Georgia,serif;font-size:25px;font-weight:700;color:var(--navy);margin-top:12px;line-height:26px;letter-spacing:1px}
.service h3 span{display:block;font-weight:400}
.service p{font-size:10.5px;line-height:13px;color:#555;margin:10px auto 0;width:220px}
.service .btn{width:118px;height:38px;margin:12px auto 0}

/* reviews */
.reviews{left:0;top:1838px;width:1200px;height:326px;background:var(--grey-review)}
.client-name{left:190px;top:2094px;width:138px;text-align:center;font-family:"Josefin Slab",Georgia,serif;font-size:13px;font-weight:700;color:var(--navy)}
.quote-mark{font-family:"Josefin Slab",Georgia,serif;font-size:70px;font-weight:700;color:var(--navy);line-height:1}
.review-text{left:380px;top:2000px;width:600px;font-size:12.5px;line-height:16px;color:#555}
.review-dots{left:624px;top:2088px;display:flex;gap:4px}
.review-dots i{width:11px;height:11px;border-radius:50%;border:1.5px solid #777}
.review-dots i.on{background:#777}

/* footer */
.foot-item{top:2192px;display:flex;align-items:center;gap:16px;color:var(--navy)}
.foot-item h4{font-family:"Josefin Slab",Georgia,serif;font-size:21px;font-weight:600;letter-spacing:.5px;line-height:22px}
.foot-item p{font-family:"Josefin Slab",Georgia,serif;font-size:14px;color:#777;letter-spacing:.5px}
.divider{top:2180px;width:1px;height:80px;background:#ddd}
.foot-wave{left:0;top:2250px;width:1200px;height:162px}
.social-foot{left:874px;top:2264px}
.copyright{left:168px;top:2360px;display:flex;align-items:center;gap:12px;font-family:"Josefin Slab",Georgia,serif;font-size:12px;font-weight:600;color:var(--white);letter-spacing:.5px}
.copyright .foot-dot{width:30px;height:30px;border-radius:50%;background:var(--white)}
.copyright a{color:var(--link);text-decoration:none}
</style>
</head>
<body>

<div class="abs hero-photo" role="img" aria-label="Photo of a smiling adviser in shirt and tie seated at a bright office desk"></div>
<svg class="abs hero-curves" viewBox="0 0 1200 700" aria-hidden="true">
  <path d="M0,0 H1200 V70 C1000,95 700,170 420,188 C300,194 220,170 170,150 L0,150 Z" fill="#fff"/>
  <path d="M170,150 C230,172 300,192 420,188 C620,180 760,150 900,130" fill="none" stroke="#1c2f56" stroke-width="5" stroke-linecap="round"/>
  <path d="M200,140 C400,160 650,130 880,118" fill="none" stroke="#bfbfbf" stroke-width="2"/>
  <path d="M0,560 C160,620 330,640 480,625 C700,600 900,560 1200,530 V700 H0 Z" fill="#fff"/>
  <path d="M440,628 C650,605 880,560 1080,545" fill="none" stroke="#1c2f56" stroke-width="5" stroke-linecap="round"/>
  <path d="M200,610 C500,640 800,590 1150,560" fill="none" stroke="#c8c8c8" stroke-width="2"/>
</svg>

<header>
  <div class="abs brand">
    <span class="brand-dot"></span>
    <span class="brand-name">GARETH PEMBLEWICK<small>CHARTERED TAX ADVISER</small></span>
  </div>
  <nav class="abs nav">
    <a class="active" href="#">HOME</a><a href="#">ABOUT</a><a href="#">CAREER</a><a href="#">BLOG</a><a href="#">NEWS</a><a href="#">CONTACT</a>
  </nav>
  <div class="abs social social-top"><span></span><span></span><span></span><span></span></div>
</header>

<section>
  <p class="abs hero-lead slab">WE WILL SHOW YOU THE WAY TO</p>
  <h1 class="abs hero-title slab">SUCCESS !</h1>
  <a class="abs btn hero-btn" href="#">REACH US NOW</a>
  <div class="abs dots hero-dots"><i class="on"></i><i></i><i></i></div>
  <div class="abs hero-contact">
    <div><span class="hex-ico"><svg width="11" height="11" viewBox="0 0 24 24"><path fill="#fff" d="M6.6 10.8a15 15 0 0 0 6.6 6.6l2.2-2.2c.3-.3.7-.4 1-.2 1.1.4 2.3.6 3.6.6.6 0 1 .4 1 1V20c0 .6-.4 1-1 1A17 17 0 0 1 3 4c0-.6.4-1 1-1h3.5c.6 0 1 .4 1 1 0 1.3.2 2.5.6 3.6.1.3 0 .7-.2 1z"/></svg></span>087 1000 2468</div>
    <div><span class="hex-ico"><svg width="11" height="9" viewBox="0 0 22 16"><rect x="1" y="1" width="20" height="14" fill="none" stroke="#fff" stroke-width="2"/><path d="M1 1l10 8 10-8" fill="none" stroke="#fff" stroke-width="2"/></svg></span>mail@pemblewick.example</div>
    <div><span class="hex-ico"><svg width="9" height="12" viewBox="0 0 18 24"><path fill="#fff" d="M9 0a9 9 0 0 0-9 9c0 7 9 15 9 15s9-8 9-15a9 9 0 0 0-9-9zm0 12a3 3 0 1 1 0-6 3 3 0 0 1 0 6z"/></svg></span>12 Elm Row, Oakford UK</div>
  </div>
</section>

<h2 class="abs statement">BEAUTIFUL <b>WORK</b><br>BY <b>PASSIONATE</b><br>PEOPLE.</h2>

<section>
  <div class="abs welcome"></div>
  <div class="abs welcome-title"><h2>WELCOME !</h2><p>GARETH PEMBLEWICK</p></div>
  <p class="abs welcome-text">Lorem ipsum dolor sit amet, consectetuer adipiscing elit, sed diam nonummy nibh euismod tincidunt ut laoreet dolore magna aliquam erat volutpat. Ut wisi enim ad minim veniam, quis nostrud exerci tation they a ullamcorpera th suscipit lobortis nisl tum zzril delenit augue duis dolore te feugait to the as.</p>
  <a class="abs btn welcome-btn" href="#">READ MORE</a>
</section>

<section>
  <h2 class="abs section-title" style="top:1246px">CHARTERED TAX ADVISER</h2>
  <p class="abs section-sub" style="top:1298px">LOREM IPSUM DOLOR SIT AMET, CONSECTETUER ELIT</p>

  <div class="abs service" style="left:173px;top:1352px">
    <svg width="216" height="242" viewBox="0 0 216 242" role="img" aria-label="Photo of business people reviewing charts at a meeting table"><defs><linearGradient id="g1" x1="0" y1="0" x2="1" y2="1"><stop offset="0" stop-color="#e8ecf0"/><stop offset="1" stop-color="#7f8fa3"/></linearGradient></defs><polygon points="108,2 214,62 214,180 108,240 2,180 2,62" fill="url(#g1)" stroke="#1c2f56" stroke-width="3"/></svg>
    <h3>INVESTMENT<span>MANAGEMENT</span></h3>
    <p>Lorem ipsum dolor sit amet, consectetueasy adipiscing elit, sed diam nonummy nibh euism tincidunt uter as laoreet dolore magna aliquam</p>
    <a class="btn" href="#">READ MORE</a>
  </div>
  <div class="abs service" style="left:478px;top:1352px">
    <svg width="216" height="242" viewBox="0 0 216 242" role="img" aria-label="Photo of two advisers in suits discussing a plan"><defs><linearGradient id="g2" x1="0" y1="0" x2="1" y2="1"><stop offset="0" stop-color="#eef0f2"/><stop offset="1" stop-color="#6d7480"/></linearGradient></defs><polygon points="108,2 214,62 214,180 108,240 2,180 2,62" fill="url(#g2)" stroke="#1c2f56" stroke-width="3"/></svg>
    <h3>WEALTH<span>MANAGEMENT</span></h3>
    <p>Lorem ipsum dolor sit amet, consectetueasy adipiscing elit, sed diam nonummy nibh euism tincidunt uter as laoreet dolore magna aliquam</p>
    <a class="btn" href="#">READ MORE</a>
  </div>
  <div class="abs service" style="left:783px;top:1352px">
    <svg width="216" height="242" viewBox="0 0 216 242" role="img" aria-label="Photo of a team pointing at a presentation board"><defs><linearGradient id="g3" x1="0" y1="0" x2="1" y2="1"><stop offset="0" stop-color="#f1f1ef"/><stop offset="1" stop-color="#a9a39a"/></linearGradient></defs><polygon points="108,2 214,62 214,180 108,240 2,180 2,62" fill="url(#g3)" stroke="#1c2f56" stroke-width="3"/></svg>
    <h3>TAX<span>ADVISORY</span></h3>
    <p>Lorem ipsum dolor sit amet, consectetueasy adipiscing elit, sed diam nonummy nibh euism tincidunt uter as laoreet dolore magna aliquam</p>
    <a class="btn" href="#">READ MORE</a>
  </div>
</section>

<section>
  <div class="abs reviews"></div>
  <h2 class="abs section-title" style="top:1872px">HAPPY CLIENTS REVIEWS</h2>
  <p class="abs section-sub" style="top:1920px">LOREM IPSUM DOLOR SIT AMET, CONSECTETUER ELIT</p>
  <svg class="abs" style="left:202px;top:1956px" width="108" height="122" viewBox="0 0 108 122" role="img" aria-label="Portrait photo of a smiling client"><polygon points="54,2 106,31 106,91 54,120 2,91 2,31" fill="#fff" stroke="#1c2f56" stroke-width="3"/><polygon points="54,9 100,35 100,87 54,113 8,87 8,35" fill="#b9a89a"/></svg>
  <p class="abs client-name">MISS. CLARA</p>
  <span class="abs quote-mark" style="left:336px;top:1962px">“</span>
  <p class="abs review-text">Lorem ipsum dolor sit amet, consectetuer adipiscing elit, sed diam nonummy nibh euismod tincidunt ut as laoreet dolore magna aliquam erat volutpat. Ut wisi enim ad minim veniam, quis nostrud exerci tation they a ullamcorper suscipit lobortis nisl ut aliquip ex ea commodo consequat. Duis autem vel eum iriure dolor in as</p>
  <span class="abs quote-mark" style="left:962px;top:2036px">”</span>
  <div class="abs review-dots"><i></i><i class="on"></i><i></i></div>
</section>

<footer>
  <div class="abs foot-item" style="left:170px">
    <span class="brand-dot" style="width:50px;height:50px"></span>
    <div><h4>GARETH PEMBLEWICK</h4><p>12 ELM ROW, OAKFORD UK</p></div>
  </div>
  <div class="abs divider" style="left:487px"></div>
  <div class="abs foot-item" style="left:524px">
    <svg width="54" height="50" viewBox="0 0 24 24" aria-hidden="true"><path fill="#1c2f56" d="M6.6 10.8a15 15 0 0 0 6.6 6.6l2.2-2.2c.3-.3.7-.4 1-.2 1.1.4 2.3.6 3.6.6.6 0 1 .4 1 1V20c0 .6-.4 1-1 1A17 17 0 0 1 3 4c0-.6.4-1 1-1h3.5c.6 0 1 .4 1 1 0 1.3.2 2.5.6 3.6.1.3 0 .7-.2 1z"/></svg>
    <div><h4>CALL US NOW</h4><p>087 1000 2468</p></div>
  </div>
  <div class="abs divider" style="left:775px"></div>
  <div class="abs foot-item" style="left:810px">
    <svg width="58" height="44" viewBox="0 0 58 44" aria-hidden="true"><rect x="3" y="10" width="46" height="30" fill="none" stroke="#1c2f56" stroke-width="3"/><path d="M3 10l23 18 23-18" fill="none" stroke="#1c2f56" stroke-width="3"/><path d="M34 6 L55 2" stroke="#1c2f56" stroke-width="2"/></svg>
    <div><h4>SEND US MAIL</h4><p>MAIL@PEMBLEWICK.EXAMPLE</p></div>
  </div>

  <svg class="abs foot-wave" viewBox="0 0 1200 162" preserveAspectRatio="none" aria-hidden="true">
    <path d="M0,40 C300,20 600,40 1200,58 V162 H0 Z" fill="#c9c9c9"/>
    <path d="M0,60 C350,95 700,80 1200,70 V162 H0 Z" fill="#fff"/>
    <path d="M0,78 C400,112 800,100 1200,88 V162 H0 Z" fill="#1c2f56"/>
    <path d="M60,70 C400,98 800,86 1200,76" fill="none" stroke="#bfbfbf" stroke-width="2"/>
  </svg>
  <div class="abs social social-foot"><span></span><span></span><span></span><span></span></div>
  <div class="abs copyright"><span class="foot-dot"></span><span>GARETH PEMBLEWICK © 2014 <a href="#">PRIVACY POLICY</a></span></div>
</footer>

</body>
</html>
```